MD Business Card

I want to create a simple business card.
I am a consultant. I design and develop furniture, lighting and accessories for hospitality and retail brands.
I want the card to be simple and clean. Not too much of a logo - but it needs the basic information shown on the attached file.
Also - I have shown some fonts that I like on the attached file.
The card can be square or rectangle. It should be double sided.
I prefer 1-2 colors (not too colorful - but using color an an accent) Even if using color on the edges as an accent.

My snapquilt link shows some other graphics styles that I like. I like clean and simple.
http://www.snapquilt.com/marendowsett/business-cards/

Reason: I needed a few more days to see some of the options evolve.

Hospitality

```html
<!DOCTYPE html>
<html lang="en">
<head>
<meta charset="utf-8">
<title>Maren Dowsett – Business Card</title>
<link rel="stylesheet" href="https://fonts.googleapis.com/css2?family=Libre+Franklin:wght@600;700&display=swap">
<style>
  :root {
    --backdrop: #e6e7e8;
    --card: #ffffff;
    --ink: #bdbfc1;
    --ink-soft: #c6c8ca;
    --rule: #e2e3e4;
  }
  html, body {
    margin: 0;
    padding: 0;
    width: 1200px;
    height: 1000px;
    overflow: hidden;
    background: var(--backdrop);
    font-family: "Libre Franklin", "Franklin Gothic Medium", Arial, sans-serif;
  }
  .sheet {
    position: relative;
    width: 1200px;
    height: 1000px;
  }
  .card {
    position: absolute;
    left: 263px;
    width: 674px;
    height: 311px;
    background: var(--card);
    box-sizing: border-box;
  }
  .card--front { top: 150px; }
  .card--back  { top: 540px; }

  .identity {
    position: absolute;
    right: 54px;
    top: 172px;
    text-align: right;
    color: var(--ink);
    padding-right: 0;
  }
  .identity__name {
    margin: 0;
    font-weight: 700;
    font-size: 46px;
    line-height: 40px;
    letter-spacing: 0.2px;
    text-transform: uppercase;
  }
  .identity__tagline {
    margin: 2px 0 0;
    font-weight: 700;
    font-size: 13px;
    letter-spacing: 0.3px;
    color: var(--ink-soft);
  }
  .identity__rule {
    position: absolute;
    right: 47px;
    top: 162px;
    width: 1px;
    height: 114px;
    background: var(--rule);
  }

  .contact {
    position: absolute;
    left: 63px;
    top: 178px;
    color: var(--ink);
  }
  .contact__line {
    margin: 0;
    font-weight: 700;
    font-size: 27px;
    line-height: 29px;
  }
  .contact__services {
    margin: 10px 0 0;
    font-weight: 700;
    font-size: 14.5px;
    color: var(--ink-soft);
  }
  .contact__divider {
    display: inline-block;
    width: 1px;
    height: 14px;
    margin: 0 4px;
    vertical-align: -2px;
    background: var(--ink-soft);
  }
</style>
</head>
<body>
<main class="sheet">
  <section class="card card--front" aria-label="Card front">
    <span class="identity__rule"></span>
    <div class="identity">
      <h1 class="identity__name">Maren<br>Dowsett</h1>
      <p class="identity__tagline">hospitality &amp; home</p>
    </div>
  </section>

  <section class="card card--back" aria-label="Card back">
    <div class="contact">
      <p class="contact__line">maren@marendowsett.com</p>
      <p class="contact__line">917.555.0148</p>
      <p class="contact__services">furniture, fixtures &amp; equipment<span class="contact__divider"></span>lighting<span class="contact__divider"></span>textiles</p>
    </div>
  </section>
</main>
</body>
</html>
```